Quenderil - Still Grace Cosmetics

Please design a logo and business cards for new food supplements, cosmetics and herbal fixatives. The products are produced ecologically and biologically in the South Tyrol and Trentino alps. The products are pure and noble. Quenderil = pure vitality Colors Background: dark or black matt (soft touch) Logodesign: powerful, elegant, violet with glossy foil The logo and design should convey warmth, passion and the 6th sense, you should get the impression that you can smell the herbal odor , Logo and business cards for new food supplements, cosmetics and herbal fixatives. The products are produced ecologically and biologically in the South Tyrol and Trentino alps. The products are pure and noble. Quenderil = pure vitality Colors Background: dark or black matt (softtouch) Logodesign: powerful elegant violet with glossy foil The logo and design is meant to convey warmth, passion and the 6th sense, you should get the impression that you can smell the herbal perfume.

Target Market(s)

Food, food supplements, vitality, health

Contact Information for Business Card

Please provide an elegant darf design that is puristic, but has a very good logo design
Elegantes dunkles design, puristisch

Logo Text

Quenderil - still Grace

Colors
6b449b

Requirements
Must have
• SVG Files Alpha channel for foil embossing High-quality design
Nice to have
• Pure elegance
Should not have
• to colorful colors

```html
<!DOCTYPE html>
<html lang="en">
<head>
<meta charset="utf-8">
<title>Quenderil – Business Card</title>
<link rel="stylesheet" href="https://fonts.googleapis.com/css2?family=Questrial&display=swap">
<style>
  :root {
    --sheet: #d6d5d3;
    --guide: #8a8a8a;
    --card-light: #ffffff;
    --card-dark: #0a0a0a;
    --ink: #0b0b0b;
    --paper-ink: #ffffff;
    --violet: #b41dc4;
    --violet-deep: #7c0c88;
    --violet-glow: #c63ad3;
  }
  * { margin: 0; padding: 0; box-sizing: border-box; }
  html, body {
    width: 1028px;
    height: 1200px;
    overflow: hidden;
    background: var(--sheet);
    font-family: "Questrial", "Century Gothic", sans-serif;
  }
  .sheet { position: relative; width: 1028px; height: 1200px; }
  .guide {
    position: absolute;
    top: 0;
    width: 0;
    height: 1200px;
    border-left: 1px dashed var(--guide);
  }
  .guide--left { left: 35px; }
  .guide--right { left: 994px; }

  .card {
    position: absolute;
    left: 35px;
    width: 960px;
    height: 548px;
  }
  .card--front { top: 35px; background: var(--card-light); }
  .card--back { top: 618px; background: var(--card-dark); }

  .brand-mark {
    position: absolute;
    width: 230px;
    height: 230px;
    border-radius: 50%;
    background: radial-gradient(circle at 55% 45%, var(--violet-glow), var(--violet-deep) 80%);
  }
  .card--front .brand-mark { left: 161px; top: 134px; }
  .card--back .brand-mark { left: 365px; top: 122px; }

  .wordmark {
    position: absolute;
    font-size: 80px;
    line-height: 1;
    font-weight: 400;
    letter-spacing: 1px;
    white-space: nowrap;
  }
  .card--front .wordmark { left: 436px; top: 208px; color: var(--ink); }
  .card--back .wordmark {
    left: 0; right: 0; top: 390px;
    text-align: center;
    color: var(--paper-ink);
  }

  .tagline {
    position: absolute;
    left: 438px;
    top: 295px;
    font-size: 26px;
    font-style: italic;
    color: var(--violet);
    white-space: nowrap;
  }

  .contact {
    position: absolute;
    top: 418px;
    left: 300px;
    display: grid;
    grid-template-columns: 172px auto;
    column-gap: 13px;
    row-gap: 5px;
    font-size: 21px;
    line-height: 23px;
  }
  .contact dt { text-align: right; color: var(--ink); }
  .contact dd { color: var(--violet); }
</style>
</head>
<body>
<div class="sheet">
  <span class="guide guide--left"></span>
  <span class="guide guide--right"></span>

  <section class="card card--front">
    <div class="brand-mark" aria-hidden="true"></div>
    <div class="wordmark">Quenderil</div>
    <div class="tagline">Still Grace Cosmetics</div>
    <dl class="contact">
      <dt>Name</dt><dd>Elsa Brunner</dd>
      <dt>Phone Number</dt><dd>0471 552 908</dd>
      <dt>Email Adress</dt><dd>elsa@quenderil.com</dd>
    </dl>
  </section>

  <section class="card card--back">
    <div class="brand-mark" aria-hidden="true"></div>
    <div class="wordmark">Quenderil</div>
  </section>
</div>
</body>
</html>
```